Pull Up Banner - Recruitment Company

We would like a design for a pull up banner.

For context: we are a recruitment business. We specialise in helping people in healthcare industry to find jobs in Australia.

I have come up with several ideas and text for the banner. Feel free to use the following as you see appropriate:

- Our logo (see attached)
- 'Healthcare Recruitment Agency'
- Some sort of imagine / cartoon of medical professionals (ie. doctor, nurse, physiotherapist, speech pathologist). A cartoon is more friendly than committing to a photo
- 'Empowering your next career move'
- 'Discover tailored opportunities based on your career preferences'
- Dot points (allied health, nursing, medical imaging)
- Contact info at the bottom including our website (www.pellatalent.com.au, our Instagram handle @pellatalent, Mobile: XXXX XXX XXX. The title section for contact information could be 'Get in touch:'

Feel free to submit a couple of designs and we can merge aspects that look good on your designs and find the perfect fit.
Thank you
Updates

Hello,

Thank you for your initial submissions to this project. I appreciate the time you've invested.

After reviewing the first attempt, I'd like to share some feedback and initial observations:

- Professionalism and engagement: Is the overall appearance of the banner professional? It's crucial that we have a high-quality design as this will represent our business.

- Image selection: The image (whether cartoon or real people) appears quite generic. Please consider submitting the banner with a few different photos in the middle for us to choose from. Ensure the image is a good fit and not simply a generic stock photo.

- Contact section: Kindly remove the phone number; we no longer wish to include it on the banner. Instead, please include our website (www.pellatalent.com.au) and Instagram handle (@pellatalent).

- Color scheme: White, black, and red/pink are preferred, or alternatively, blue. However, please avoid incorporating too many different colors as it may detract from the professional appearance.

We will be printing the design on a banner and require it to look professional and engaging.

Thank you once again for your submissions. I hope the feedback provided above is helpful.

Warm regards,

Target Market(s)

Allied Health Australia

Font styles to use
Serif

Colors
0054AA
0677BA
7BADD7
CADEEF
E8F1F8
0094D4
00A9DD
6FCCEA
C7EBF8
E9F6FB
EB3D1F
EC4F4E
F09395
F8D3D4
FCEDEE

```html
<!DOCTYPE html>
<html lang="en">
<head>
<meta charset="utf-8">
<title>Pella Talent – Pull Up Banner</title>
<link href="https://fonts.googleapis.com/css2?family=Tinos:wght@400;700&family=Montserrat:wght@500&display=swap" rel="stylesheet">
<style>
  :root {
    --page-bg: #ebeae8;
    --banner-white: #f7f7f7;
    --ink: #0d0d0d;
    --panel-dark: #080808;
    --brand-blue: #4a97cf;
    --scrub-light: #7fb0d2;
    --scrub-dark: #3f6d9c;
    --corridor: #2b313b;
    --text-light: #f2f2f2;
    --icon-ink: #1a1a1a;
  }
  * { margin: 0; padding: 0; box-sizing: border-box; }
  html, body { width: 1200px; height: 1200px; overflow: hidden; }
  body { background: var(--page-bg); position: relative; font-family: "Tinos", "Times New Roman", serif; }

  .banner {
    position: absolute; left: 380px; top: 25px;
    width: 440px; height: 1150px;
    background: var(--panel-dark);
    overflow: hidden;
    box-shadow: 0 6px 24px rgba(0,0,0,.12);
  }
  .hero-photo {
    position: absolute; left: 0; top: 260px; width: 440px; height: 492px;
    background:
      radial-gradient(ellipse 48% 42% at 50% 72%, var(--scrub-light) 0%, rgba(127,176,210,0) 100%),
      radial-gradient(ellipse 70% 50% at 50% 78%, var(--scrub-dark) 0%, rgba(63,109,156,0) 100%),
      linear-gradient(180deg, #3a414c 0%, var(--corridor) 40%, #151a21 100%);
  }
  .header-curve { position: absolute; left: 0; top: 0; width: 440px; height: 400px; }

  .brand { position: absolute; left: 0; top: 46px; width: 440px; text-align: center; }
  .brand-name {
    font-family: "Tinos", serif; font-weight: 700; font-size: 46px;
    letter-spacing: 5px; color: var(--ink); line-height: 1;
  }
  .brand-tagline {
    margin-top: 16px; font-family: "Montserrat", sans-serif; font-weight: 500;
    font-size: 11px; letter-spacing: 2.4px; color: var(--ink);
  }
  .headline {
    position: absolute; left: 0; top: 152px; width: 440px; text-align: center;
    font-weight: 700; font-size: 37px; line-height: 1.12; letter-spacing: -1.4px;
    color: var(--ink); text-transform: uppercase;
  }
  .subline {
    position: absolute; left: 60px; top: 248px; width: 320px; text-align: center;
    font-size: 24px; line-height: 0.98; color: var(--ink);
  }

  .specialties {
    position: absolute; left: 20px; top: 776px; width: 400px; height: 170px;
    display: flex; justify-content: space-between;
  }
  .specialty { width: 120px; display: flex; flex-direction: column; align-items: center; }
  .specialty-badge { width: 86px; height: 86px; }
  .specialty-label {
    margin-top: 18px; font-size: 24px; line-height: 1; text-align: center; color: var(--text-light);
  }
  .divider { width: 0; height: 150px; margin-top: 8px; border-left: 1.5px dashed var(--brand-blue); }

  .contact-band {
    position: absolute; left: 0; top: 954px; width: 440px; height: 40px;
    background: var(--brand-blue); display: flex; align-items: center; justify-content: center;
    font-weight: 700; font-size: 21px; color: var(--text-light); letter-spacing: -0.3px;
  }
  .contact {
    position: absolute; left: 0; top: 1014px; width: 440px; text-align: center;
    color: var(--text-light); font-size: 24px; line-height: 1;
  }
  .contact-social { display: flex; align-items: center; justify-content: center; gap: 10px; }
  .social-dot { width: 18px; height: 18px; border-radius: 50%; border: 2.5px solid var(--brand-blue); }
  .contact-web { margin-top: 22px; letter-spacing: 0.3px; }
</style>
</head>
<body>
  <main class="banner">
    <div class="hero-photo" role="img" aria-label="Photo of a team of five healthcare workers in blue scrubs standing in a hospital corridor"></div>

    <svg class="header-curve" viewBox="0 0 440 400" aria-hidden="true">
      <path d="M0 0 H440 V322 Q220 430 0 355 Z" fill="var(--brand-blue)"/>
      <path d="M0 0 H440 V300 Q220 418 0 292 Z" fill="var(--banner-white)"/>
    </svg>

    <header class="brand">
      <div class="brand-name">PELLA TALENT</div>
      <div class="brand-tagline">HEALTHCARE RECRUITMENT AGENCY</div>
    </header>

    <h1 class="headline">Empowering your<br>next career move</h1>
    <p class="subline">Discover tailored opportunities based on your career preferences</p>

    <section class="specialties">
      <div class="specialty">
        <svg class="specialty-badge" viewBox="0 0 86 86" role="img" aria-label="Allied health icon">
          <circle cx="43" cy="43" r="41" fill="#fff"/>
          <circle cx="43" cy="43" r="35" fill="var(--panel-dark)"/>
          <path d="M8 52 A35 35 0 0 0 78 52 Z" fill="var(--brand-blue)"/>
          <circle cx="43" cy="43" r="28" fill="#f4f4f4"/>
          <g fill="none" stroke="var(--icon-ink)" stroke-width="1.6" stroke-linecap="round">
            <circle cx="43" cy="41" r="9" stroke-dasharray="3 3"/>
            <path d="M40 36 h6 v3 h3 v6 h-3 v3 h-6 v-3 h-3 v-6 h3 z"/>
            <path d="M26 54 q10 -6 17 0 q7 4 17 -3"/>
            <path d="M30 28 q8 -6 16 -2"/>
          </g>
        </svg>
        <div class="specialty-label">Allied<br>Health</div>
      </div>
      <div class="divider"></div>
      <div class="specialty">
        <svg class="specialty-badge" viewBox="0 0 86 86" role="img" aria-label="Nursing icon">
          <circle cx="43" cy="43" r="41" fill="#fff"/>
          <circle cx="43" cy="43" r="35" fill="var(--panel-dark)"/>
          <path d="M8 52 A35 35 0 0 0 78 52 Z" fill="var(--brand-blue)"/>
          <circle cx="43" cy="43" r="28" fill="#f4f4f4"/>
          <g fill="none" stroke="var(--icon-ink)" stroke-width="1.8" stroke-linecap="round" stroke-linejoin="round">
            <path d="M43 55 C30 46 28 38 33 33 C37 29 42 31 43 35 C44 31 49 29 53 33 C58 38 56 46 43 55 Z"/>
            <path d="M30 43 h7 l2 -4 l3 8 l2 -4 h12"/>
          </g>
        </svg>
        <div class="specialty-label">Nursing</div>
      </div>
      <div class="divider"></div>
      <div class="specialty">
        <svg class="specialty-badge" viewBox="0 0 86 86" role="img" aria-label="Medical imaging icon">
          <circle cx="43" cy="43" r="41" fill="#fff"/>
          <circle cx="43" cy="43" r="35" fill="var(--panel-dark)"/>
          <path d="M8 52 A35 35 0 0 0 78 52 Z" fill="var(--brand-blue)"/>
          <circle cx="43" cy="43" r="28" fill="#f4f4f4"/>
          <g fill="none" stroke="var(--icon-ink)" stroke-width="1.6" stroke-linecap="round">
            <rect x="32" y="27" width="22" height="30" rx="2"/>
            <rect x="38" y="24" width="10" height="5" rx="1" fill="#f4f4f4"/>
            <path d="M38 49 L48 36"/>
            <circle cx="37" cy="50" r="1.8"/>
            <circle cx="49" cy="35" r="1.8"/>
            <path d="M44 52 h6 M44 49 h6"/>
          </g>
        </svg>
        <div class="specialty-label">Medical<br>Imaging</div>
      </div>
    </section>

    <div class="contact-band">GET IN TOUCH:</div>

    <footer class="contact">
      <div class="contact-social"><span class="social-dot"></span><span>@pellatalent</span></div>
      <div class="contact-web">www.pellatalent.com.au</div>
    </footer>
  </main>
</body>
</html>
```